Aviation Law Firm Needs Envelope Design

The envelope design must be EYE CATCHING and sexy, yet very professional. The information in the return address should be in the upper left hand corner and read:
The Marrow Law Firm
P.O. Box 9187
Lakeland, Florida 33912

The word: "ADVERTISEMENT" must appear on the front of the envelope in some fashion.

The colors should compliment the letterhead image (attached). However, I would like for the envelope to remain white or light colored in the upper right hand corner so that the post office can read any stamps, etc.

Target Market(s)

Pilots; Legal Clients

Industry/Entity Type

Law Firm

Font styles to use
Serif
Sans Serif

Colors
191919
fbee3e
ffffff

Requirements
Must have
• Must capture the use of the entire envelope, BUT leave space for receiver's address and post office stamps, etc.

```html
<!DOCTYPE html>
<html lang="en">
<head>
<meta charset="UTF-8">
<title>The Marrow Law Firm – Envelope</title>
<link rel="stylesheet" href="https://fonts.googleapis.com/css2?family=Playfair+Display:wght@700&family=Montserrat:wght@500;700&display=swap">
<style>
  :root {
    --backdrop: #a9a3a0;
    --envelope: #191919;
    --accent: #fbee3e;
    --paper: #ffffff;
    --mark-tint: #2d2a0e;
    --flap-line: #0c0c0c;
    --soft-text: #d9d9d9;
  }
  html, body {
    margin: 0;
    width: 1200px;
    height: 1200px;
    overflow: hidden;
    background: var(--backdrop);
  }
  .envelope {
    position: absolute;
    left: 50px;
    top: 361px;
    width: 1100px;
    height: 478px;
    background: var(--envelope);
    overflow: hidden;
  }
  .envelope__flap {
    position: absolute;
    inset: 0;
    width: 100%;
    height: 100%;
  }
  .envelope__stamp-zone {
    position: absolute;
    top: 0;
    right: 0;
    width: 250px;
    height: 170px;
    background: var(--paper);
  }
  .return-address {
    position: absolute;
    left: 44px;
    top: 38px;
    margin: 0;
    font-style: normal;
    font-family: "Montserrat", Arial, sans-serif;
    font-weight: 500;
    font-size: 17px;
    line-height: 1.5;
    color: var(--soft-text);
  }
  .return-address__name {
    display: block;
    font-family: "Playfair Display", Georgia, serif;
    font-weight: 700;
    font-size: 26px;
    line-height: 1.3;
    color: var(--accent);
    margin-bottom: 4px;
  }
  .envelope__mark {
    position: absolute;
    left: 0;
    right: 0;
    top: 230px;
    margin: 0;
    text-align: center;
    font-family: "Playfair Display", Georgia, serif;
    font-weight: 700;
    font-size: 44px;
    color: var(--mark-tint);
  }
  .envelope__notice {
    position: absolute;
    left: 44px;
    bottom: 40px;
    margin: 0;
    font-family: "Montserrat", Arial, sans-serif;
    font-weight: 700;
    font-size: 20px;
    letter-spacing: 6px;
    color: var(--accent);
  }
  .envelope__edge {
    position: absolute;
    left: 0;
    right: 0;
    bottom: 0;
    height: 14px;
    background: var(--accent);
  }
</style>
</head>
<body>
  <div class="envelope">
    <svg class="envelope__flap" viewBox="0 0 1100 478" aria-hidden="true">
      <line x1="330" y1="190" x2="1060" y2="190" stroke="var(--flap-line)" stroke-width="3"/>
    </svg>
    <div class="envelope__stamp-zone"></div>
    <address class="return-address">
      <span class="return-address__name">The Marrow Law Firm</span>
      P.O. Box 9187<br>
      Lakeland, Florida 33912
    </address>
    <p class="envelope__mark">The Marrow Law Firm</p>
    <p class="envelope__notice">ADVERTISEMENT</p>
    <div class="envelope__edge"></div>
  </div>
</body>
</html>
```